Business Card Design Quandong Celebration Crafters

on the front i would like to see the logo and my contact details. on the back i would like it to include the 3 parts to the business party planning, party hire and party supplies also with a line at the bottom (or white space) to write their appointment details.

Target Market(s)

mums and corporates

Industry/Entity Type

Business

Requirements
Must have
• logo and contact details which are: Name: Rosalind, Phone: 0417365920, email: ros@quandongfetes.com.au, Website: www.quandongfetes.com.au,

```html
<!DOCTYPE html>
<html lang="en">
<head>
<meta charset="utf-8">
<title>Quandong Celebration Crafters – Business Card</title>
<link rel="stylesheet" href="https://fonts.googleapis.com/css2?family=Open+Sans:wght@400;600;700&display=swap">
<style>
  :root {
    --page: #ece9e4;
    --card: #ffffff;
    --ink: #2b2b2b;
    --ink-soft: #555555;
    --blue: #3fb3e6;
    --pink: #e2338a;
    --yellow: #f4c01e;
    --purple: #5b4a9e;
    --line-grey: #a9a9a9;
    --line-yellow: #f5dc8a;
    --line-blue: #9fd8f2;
    --line-pink: #f2b3d3;
  }
  * { box-sizing: border-box; margin: 0; padding: 0; }
  html, body {
    width: 1200px; height: 913px; overflow: hidden;
    background: var(--page);
    font-family: "Open Sans", Arial, sans-serif;
    color: var(--ink);
  }
  .canvas { position: relative; width: 1200px; height: 913px; }
  .card {
    position: absolute;
    width: 560px; height: 340px;
    background: var(--card);
    box-shadow: 0 6px 18px rgba(0,0,0,.18);
    overflow: hidden;
  }
  /* Front */
  .card--front { left: 50px; top: 90px; }
  .brand { position: absolute; left: 34px; top: 70px; width: 230px; }
  .brand__art {
    width: 150px; height: 130px; margin: 0 0 12px 30px;
    border-radius: 14px;
    background: linear-gradient(160deg, #f3b5e0 0%, #b7a3e8 45%, #d8c3ae 100%);
  }
  .brand__name {
    font-weight: 700; font-size: 26px; line-height: 1.1;
    color: var(--blue);
  }
  .contact { position: absolute; left: 300px; top: 92px; }
  .contact__name { font-weight: 700; font-size: 19px; color: var(--blue); }
  .contact__role { font-size: 12px; color: var(--ink-soft); margin-bottom: 18px; }
  .contact__list { list-style: none; font-size: 13px; color: var(--ink-soft); }
  .contact__list li { display: flex; align-items: center; gap: 12px; margin-bottom: 7px; }
  .contact__list svg { width: 13px; height: 13px; flex: none; }
  .stripe {
    position: absolute; left: 0; right: 0; bottom: 0; height: 12px;
    display: flex;
  }
  .stripe span { flex: 1; }
  .stripe .s1 { background: var(--purple); }
  .stripe .s2 { background: var(--pink); }
  .stripe .s3 { background: var(--yellow); }
  .stripe .s4 { background: var(--blue); }
  /* Back */
  .card--back { left: 590px; top: 470px; padding: 22px; }
  .services { display: flex; gap: 10px; height: 170px; }
  .service {
    flex: 1; border: 1px solid; padding: 10px 12px;
    font-size: 15px; font-weight: 400;
  }
  .service--planning { border-color: var(--line-yellow); }
  .service--hire { border-color: var(--line-blue); }
  .service--supplies { border-color: var(--line-pink); }
  .appointment {
    margin-top: 14px; height: 110px;
    border: 1px solid var(--line-grey);
    display: flex; align-items: flex-end;
  }
  .appointment__label {
    font-weight: 600; font-size: 16px;
    border-top: 1px solid var(--line-grey); border-right: 1px solid var(--line-grey);
    padding: 2px 10px;
  }
</style>
</head>
<body>
<main class="canvas">
  <section class="card card--front" aria-label="Card front">
    <div class="brand">
      <div class="brand__art" role="img" aria-label="Illustrated mascot holding colourful party balloons"></div>
      <p class="brand__name">Quandong Celebration Crafters</p>
    </div>
    <div class="contact">
      <p class="contact__name">Rosalind</p>
      <p class="contact__role">Managing Director</p>
      <ul class="contact__list">
        <li>
          <svg viewBox="0 0 16 16"><path fill="#e2338a" d="M3 2h3l1 4-2 1c1 2 2 3 4 4l1-2 4 1v3c0 1-1 2-2 2C7 15 1 9 1 4c0-1 1-2 2-2z"/></svg>
          0417365920
        </li>
        <li>
          <svg viewBox="0 0 16 16"><rect x="1" y="3" width="14" height="10" fill="#3fb3e6"/><path d="M1 3l7 6 7-6" fill="none" stroke="#fff" stroke-width="1.4"/></svg>
          ros@quandongfetes.com.au
        </li>
        <li>
          <svg viewBox="0 0 16 16"><circle cx="8" cy="8" r="7" fill="#f4c01e"/><path d="M1 8h14M8 1v14" stroke="#fff" stroke-width="1.2"/></svg>
          www.quandongfetes.com.au
        </li>
      </ul>
    </div>
    <div class="stripe"><span class="s1"></span><span class="s2"></span><span class="s3"></span><span class="s4"></span></div>
  </section>

  <section class="card card--back" aria-label="Card back">
    <div class="services">
      <div class="service service--planning">Party planning</div>
      <div class="service service--hire">Party hire</div>
      <div class="service service--supplies">Party supplies</div>
    </div>
    <div class="appointment">
      <span class="appointment__label">Appointment</span>
    </div>
  </section>
</main>
</body>
</html>
```